DOUBLE SIDED BROCHURE NEEDED TO PROMOTE DOCTOR

I need a double sided DL size (99mm x 210mm) brochure, promoting a doctor seeing patients in a new area.

I want something professional. I have included the relevant information. I would also like the Dr's picture somwhere in the brochure, with a professional background. I wish to print these tomorrow, so i will pick a winner within 14 hours of posting this ad.

I have included an example of a brochures design that I recently saw, and its definietly a good starting point.

Medical

```html
<!DOCTYPE html>
<html lang="en">
<head>
<meta charset="utf-8">
<title>Dr. Haddad – Specialist Surgeon</title>
<link rel="stylesheet" href="https://fonts.googleapis.com/css2?family=Lato:wght@400;700&display=swap">
<style>
  :root {
    --teal: #0f8a9c;
    --teal-dark: #0b7585;
    --orange: #c9531a;
    --ink: #1f2326;
    --white: #ffffff;
    --pale-top: #f4fafd;
    --pale-bottom: #cfe6f1;
    --photo-sky: #7ea8d6;
    --photo-mid: #9aa6b0;
    --photo-low: #5b6b63;
  }
  * { margin: 0; padding: 0; box-sizing: border-box; }
  html, body { width: 1200px; height: 2544px; overflow: hidden; }
  body {
    font-family: "Lato", Arial, sans-serif;
    color: var(--ink);
    background: linear-gradient(180deg, var(--pale-top) 0%, #e6f3f9 50%, var(--pale-bottom) 100%);
    position: relative;
  }
  .hero-photo {
    position: absolute; left: 0; top: 0; width: 1200px; height: 960px;
    background: linear-gradient(160deg, var(--photo-sky) 0%, #b9cde3 35%, var(--photo-mid) 65%, var(--photo-low) 100%);
  }
  .hero-wave { position: absolute; left: 0; top: 780px; width: 1200px; height: 280px; }
  .services {
    position: absolute; left: 74px; top: 1030px; width: 1070px;
    font-size: 54px; line-height: 72px; font-weight: 400;
  }
  .services ul { list-style: none; margin-left: 112px; }
  .services li { position: relative; }
  .services li::before {
    content: ""; position: absolute; left: -58px; top: 30px;
    width: 16px; height: 16px; border-radius: 50%; background: var(--ink);
  }
  .services .group-lead { margin-top: 14px; }
  .services ul.general { margin-top: 14px; }
  .services ul.general li:last-child { margin-top: 14px; }
  .referral-band {
    position: absolute; left: 0; top: 2268px; width: 1200px; height: 234px;
    background: var(--teal); color: var(--white); text-align: center;
  }
  .referral-label { font-weight: 700; font-size: 50px; line-height: 60px; padding-top: 30px; }
  .referral-number { font-weight: 700; font-size: 88px; line-height: 100px; letter-spacing: 1px; }
</style>
</head>
<body>
  <div class="hero-photo" role="img" aria-label="Photo of the surgeon in a dark jacket and glasses in front of a modern hospital building under a blue sky"></div>

  <svg class="hero-wave" viewBox="0 0 1200 280" preserveAspectRatio="none" aria-hidden="true">
    <path d="M0 70 C 300 20, 800 10, 1200 50 L1200 280 L0 280 Z" fill="var(--teal)"/>
    <path d="M0 120 C 350 70, 800 60, 1200 100 L1200 280 L0 280 Z" fill="var(--orange)"/>
    <path d="M0 165 C 350 110, 850 120, 1200 240 L1200 280 L0 280 Z" fill="#eef7fb"/>
  </svg>

  <section class="services">
    <p>Dr.Haddad is a highly trained specialised surgeon, in all areas of Endocrine, Breast and General Surgery. Including;</p>
    <ul class="endocrine">
      <li>Thyroid Surgery</li>
      <li>Parathyroid surgery<br>(including minimally invasive parathyroidectomy)</li>
      <li>Breast Cancer<br>Benign breast lesions</li>
    </ul>
    <p class="group-lead">All areas of general surgery, such as;</p>
    <ul class="general">
      <li>Gallbladder surgery</li>
      <li>Hernia surgery</li>
      <li>Haemorrhoids</li>
      <li>Carpal Tunnel</li>
      <li>Vasectomy etcetc...</li>
    </ul>
  </section>

  <footer class="referral-band">
    <p class="referral-label">Please send all referrals by fax to</p>
    <p class="referral-number">(08) 5550 4826</p>
  </footer>
</body>
</html>
```